1 x Double Page Spread for Book Design Project.

Student Wellbeing Planner Book, to be used by teenagers aged 12-18. Needs to be colourful, fun and engaging.

Require a double page spread, left and right hand page to be designed in 4 colour.

The final design should communicate positive learning in an easy to understand format.

Target Market(s)

Teenagers Aged 12-18 years old

Industry/Entity Type

Learning

Requirements
Must have
• Must have a more colourful and updated look than attached current layout.

Must have the weekly planner functionality as per the attached layout.

```html
<!DOCTYPE html>
<html lang="en">
<head>
<meta charset="utf-8">
<title>Student Wellbeing Planner – Weekly Spread</title>
<link href="https://fonts.googleapis.com/css2?family=Roboto+Condensed:wght@400;700;900&family=Arimo:wght@400;700&display=swap" rel="stylesheet">
<style>
:root{
  --magenta:#e5197e;
  --yellow:#fff200;
  --black:#1a1a1a;
  --ink:#222;
  --paper:#efeee6;
  --paper-light:#f6f5ee;
  --rule:#bdbdbd;
  --pink:#f7c9dc;
  --note:#f8f4c4;
  --green:#7cc242;
  --faint:#d4d4d0;
}
*{box-sizing:border-box;margin:0;padding:0}
html,body{width:1200px;height:854px;overflow:hidden;background:#fff}
body{position:relative;font-family:"Arimo",Arial,sans-serif;color:var(--ink)}
.page{position:absolute;top:22px;height:764px;background:linear-gradient(135deg,var(--paper-light),var(--paper));box-shadow:0 2px 6px rgba(0,0,0,.18)}
.page--left{left:22px;width:576px}
.page--right{left:598px;width:580px}
.abs{position:absolute}
.texture{position:absolute}
.splash-dark{left:22px;top:624px;width:300px;height:162px;background:linear-gradient(20deg,#2b2b2b 40%,rgba(60,60,60,.0) 100%)}
.splash-yellow{left:1056px;top:22px;width:122px;height:110px;background:linear-gradient(225deg,var(--yellow) 35%,rgba(255,242,0,0) 100%)}
.illus-pencil{left:396px;top:286px;width:86px;height:60px;background:var(--faint);opacity:.6;border-radius:6px}
.illus-hand{left:700px;top:350px;width:356px;height:286px;background:var(--faint);opacity:.55;border-radius:40px 20px 60px 20px}

.section-title{left:62px;top:70px;font:700 15.5px/1 "Arimo",Arial,sans-serif;display:flex;align-items:center;gap:3px;white-space:nowrap}
.section-title .icon{width:19px;height:19px;border:3px solid var(--black);border-radius:50%;display:inline-block}
.advice{left:62px;top:106px;width:206px;font-size:9.6px;line-height:11.2px}
.advice h3{color:var(--magenta);font-size:11px;margin-bottom:3px}
.advice b{display:block}
.advice p{margin-top:6px}
.advice p:first-of-type{margin-top:0}
.advice ul{list-style:none}
.advice li{padding-left:8px;text-indent:-8px}
.advice li::before{content:"• "}

.month-tab{top:50px;height:44px;font:700 33px/44px "Roboto Condensed",sans-serif;padding:0 8px}
.month-tab--current{left:268px;background:var(--magenta);color:#fff}
.month-tab--next{left:428px;top:54px;height:40px;line-height:40px;background:var(--yellow);color:var(--black)}
.year-tab{left:618px;top:60px;height:46px;padding:0 10px;background:var(--magenta);color:#fff;font:700 40px/46px "Roboto Condensed",sans-serif;transform:rotate(-2deg)}
.dotted{top:113px;height:0;border-top:3px dotted var(--black)}
.dotted--left{left:264px;width:334px}
.dotted--right{left:598px;width:578px}

.calendar{left:798px;top:60px;font:700 9px/11px "Arimo",Arial,sans-serif;text-align:center}
.calendar .cal-month{width:360px;text-align:center}
.calendar .cal-row{display:flex}
.calendar .cal-row span{width:12px}

.panel-head{font:700 11px/22px "Arimo",Arial,sans-serif;color:#fff}
.tick{color:var(--magenta);font-weight:700}
.day-lines{left:322px;top:146px;width:226px;height:500px;background:repeating-linear-gradient(to bottom,transparent 0 11px,var(--rule) 11px 12px)}
.day{left:326px;font:700 10px/1 "Arimo",Arial,sans-serif;background:var(--paper-light);padding-right:4px}
.weekend{font:700 10px/1 "Arimo",Arial,sans-serif;width:100px;text-align:center}

.tip-note{left:502px;top:648px;width:90px;height:84px;background:var(--note);transform:rotate(-4deg);font-size:9px;line-height:10.5px;text-align:center;padding:10px 5px 0;box-shadow:1px 1px 3px rgba(0,0,0,.2)}
.tip-note b{display:block}
.tip-pin{left:550px;top:624px;width:18px;height:18px;border-radius:50%;background:var(--green);border:2px solid #4a7c25}

.vocab{left:40px;top:640px;width:206px;height:66px;background:#fff;transform:rotate(-3deg);padding:4px 8px;font-size:12px;line-height:13px}
.vocab h4{font:700 12px/1 "Roboto Condensed",sans-serif;margin-bottom:2px}
.vocab .cols{display:grid;grid-template-columns:72px 58px 70px}
.rate{left:96px;top:716px;width:198px;height:52px;background:#fff;padding:4px 8px;font-size:12px}
.rate h4{font:700 13px/1 "Roboto Condensed",sans-serif}
.rate .scale{margin-top:6px;word-spacing:6px}
.folio{height:24px;padding:0 4px;background:var(--yellow);font:700 15px/24px "Roboto Condensed",sans-serif;color:var(--black)}

.todo-panel{left:630px;top:118px;width:516px;height:632px;border:6px solid var(--black);border-radius:12px;background:#fff;overflow:hidden}
.todo-head{height:20px;background:var(--black);display:flex;align-items:center;gap:10px;padding-left:8px;font:400 11px/1 "Arimo",Arial,sans-serif;color:#fff}
.todo-head .value-label{background:var(--magenta);padding:2px 4px;font-weight:700;margin-left:110px}
.todo-head .done-col{margin-left:auto;width:40px;font-size:6px;text-align:center;color:var(--magenta)}
.todo-rows{position:absolute;left:0;top:20px;width:100%}
.todo-row{height:24px;border-bottom:1px solid var(--rule);display:flex;font-size:9px}
.todo-row .write{flex:1;padding:2px 4px;display:flex;justify-content:space-between}
.todo-row .done{width:14px;border-left:1px solid var(--black)}
.todo-row .num{width:20px;border-left:1px solid var(--black);text-align:center;font:700 10px/24px "Arimo",Arial,sans-serif}
.todo-row--pink .write{background:var(--pink)}
.this-week{left:716px;top:746px;width:200px;padding:3px 6px;background:#fff;transform:rotate(-2deg);font-size:10px;line-height:12px}
</style>
</head>
<body>

<section class="page page--left"></section>
<section class="page page--right"></section>

<div class="texture splash-dark" role="img" aria-label="Black ink splatter decoration"></div>
<div class="texture splash-yellow" role="img" aria-label="Yellow paint splash decoration"></div>

<h1 class="abs section-title">Career &amp; <span class="icon" role="img" aria-label="Alarm clock icon"></span> management</h1>

<div class="abs advice">
  <h3>Procrastination/Decision Making</h3>
  <p>How easy is it to delay doing things?<br>Why do you do it?</p>
  <b>Gulosus umbraculi quod</b>
  <ul>
    <li>quadrupei prae parsim onia</li>
    <li>chirographi, semper fragilis umbr</li>
    <li>saetosus syrtes, quod Caesar umgrediet</li>
    <li>quadrupei praem uniet parsi</li>
    <li>chirographi, semper fragilis umbr</li>
    <li>saetosus syrtes, quod Caesar cirdiet</li>
    <li>quadrupei praemuniet parsimonia</li>
    <li>chirographi, semper fragilis umbraculi</li>
  </ul>
  <p>Matrimonii. Catelli iocari oratori, etiam agri colae spino sus conubium santet perspicax syrtes.</p>
  <p>Quapei praniet parsimonia conne aegre sp am pat matrimonii</p>
  <ul>
    <li>chirographi, semper fragilis umbr adqu</li>
    <li>saetosus syrtes, quod Caesar oncubine aegre nosus amputat maonii</li>
    <li>quadrupei praemuniet pimonia</li>
    <li>chirographi, semper fragilis umbuli adq</li>
    <li>chirographi, semper gilis</li>
    <li>saetosus syrtes, quod Caesar circ</li>
    <li>quadrupei praemuniet pars</li>
    <li>chirographi, semper umbraculi adquireret</li>
    <li>chirographi, semper fragilis umbr</li>
  </ul>
  <p><b>Positive talk is beneficial</b></p>
  <ul>
    <li>quadrupei prat parsimonia hirographi, semper fragilis umbraculi adqeret</li>
    <li>saetosus syrtes, quod Caesar cgrediet</li>
  </ul>
  <p>Beware of the “bouncing effect”</p>
  <ul>
    <li>adrupei pmuniet parmonia</li>
    <li>chirographi, semper frag umbraculi</li>
    <li>saetosus syrtes, quod Caesar circumgrediet</li>
  </ul>
  <p>Committing yourself immediately to one task</p>
  <ul>
    <li>quadrupei praemuniet parsimonia</li>
    <li>chirographi, semper fragilis umbraculi</li>
  </ul>
  <p>Quadrupei praiet paronia hirog, semper fra gilis um aculi adquret</p>
  <ul><li>Seaetosus syrtes, quod Caesar circumgrediet</li></ul>
</div>

<div class="abs month-tab month-tab--current">September</div>
<div class="abs month-tab month-tab--next">/ August</div>
<div class="abs dotted dotted--left"></div>

<div class="abs priorities" style="left:0;top:0;width:600px;height:854px">
  <svg width="600" height="854" viewBox="0 0 600 854" style="position:absolute;left:0;top:0">
    <path d="M328 118 H560 Q574 118 574 132 V648 L442 788 L314 648 V132 Q314 118 328 118 Z" fill="var(--black)"/>
    <path d="M322 140 H566 V645 L442 776 L322 645 Z" fill="var(--paper-light)"/>
    <line x1="548" y1="140" x2="548" y2="645" stroke="var(--black)" stroke-width="1.5"/>
    <line x1="337" y1="672" x2="547" y2="672" stroke="var(--rule)"/>
    <line x1="362" y1="686" x2="522" y2="686" stroke="var(--black)" stroke-width="1.5"/>
    <line x1="390" y1="716" x2="494" y2="716" stroke="var(--rule)"/>
    <line x1="412" y1="740" x2="472" y2="740" stroke="var(--rule)"/>
  </svg>
  <div class="abs panel-head" style="left:324px;top:118px">Priorties/Due dates</div>
  <div class="abs tick" style="left:548px;top:116px;font-size:18px">✔</div>
  <div class="abs day-lines"></div>
  <div class="abs texture illus-pencil" role="img" aria-label="Faint pencil sketch"></div>
  <div class="abs day" style="top:144px">Monday 27th</div>
  <div class="abs day" style="top:244px">Tuesday 28th</div>
  <div class="abs day" style="top:345px">Wednesday 29th</div>
  <div class="abs day" style="top:447px">Thursday 30th</div>
  <div class="abs day" style="top:548px">Friday 31st</div>
  <div class="abs weekend" style="left:390px;top:653px">Saturday</div>
  <div class="abs weekend" style="left:390px;top:692px">Sunday</div>
</div>

<div class="abs tip-note"><b>Well being tip:</b>Lifestyle is a combintaion of exercise, attitude and diet; get it right.</div>
<div class="abs tip-pin"></div>

<div class="abs vocab">
  <h4>Vocabulary Builder</h4>
  <div class="cols">
    <span>matted<br>guaranteed<br>imaginative</span>
    <span>draught<br>jettison<br>barely</span>
    <span>hilarious<br>pincer<br>category</span>
  </div>
</div>
<div class="abs rate">
  <h4>Rate your week</h4>
  <div style="font-size:11px"><i>1</i> - Fair to <i>10</i> Great</div>
  <div class="scale">1 2 3 4 5 6 7 8 9 10</div>
</div>
<div class="abs folio" style="left:36px;top:750px">96</div>

<div class="abs year-tab">2013</div>
<div class="abs calendar">
  <div class="cal-month">September</div>
  <div class="cal-row"><span>S</span><span>S</span><span>M</span><span>T</span><span>W</span><span>T</span><span>F</span><span>S</span><span>S</span><span>M</span><span>T</span><span>W</span><span>T</span><span>F</span><span>S</span><span>S</span><span>M</span><span>T</span><span>W</span><span>T</span><span>F</span><span>S</span><span>S</span><span>M</span><span>T</span><span>W</span><span>T</span><span>F</span><span>S</span><span>S</span></div>
  <div class="cal-row"><span>1</span><span>2</span><span>3</span><span>4</span><span>5</span><span>6</span><span>7</span><span>8</span><span>9</span><span>10</span><span>11</span><span>12</span><span>13</span><span>14</span><span>15</span><span>16</span><span>17</span><span>18</span><span>19</span><span>20</span><span>21</span><span>22</span><span>23</span><span>24</span><span>25</span><span>26</span><span>27</span><span>28</span><span>29</span><span>30</span></div>
</div>
<div class="abs dotted dotted--right"></div>

<div class="abs todo-panel">
  <div class="todo-head">
    <span>Things to do</span>
    <span class="value-label">Value for life:</span>
    <span>Enthusiasm</span>
    <span class="done-col">Done ✔ Home use</span>
  </div>
  <div class="todo-rows">
    <div class="todo-row"><span class="write"></span><span class="done"></span><span class="num">1</span></div>
    <div class="todo-row"><span class="write"></span><span class="done"></span><span class="num">2</span></div>
    <div class="todo-row"><span class="write"></span><span class="done"></span><span class="num">3</span></div>
    <div class="todo-row"><span class="write"></span><span class="done"></span><span class="num">4</span></div>
    <div class="todo-row"><span class="write"></span><span class="done"></span><span class="num">5</span></div>
    <div class="todo-row"><span class="write"></span><span class="done"></span><span class="num">6</span></div>
    <div class="todo-row"><span class="write"></span><span class="done"></span><span class="num">7</span></div>
    <div class="todo-row"><span class="write"></span><span class="done"></span><span class="num">8</span></div>
    <div class="todo-row"><span class="write"></span><span class="done"></span><span class="num">9</span></div>
    <div class="todo-row"><span class="write"></span><span class="done"></span><span class="num">10</span></div>
    <div class="todo-row"><span class="write"></span><span class="done"></span><span class="num">11</span></div>
    <div class="todo-row"><span class="write"></span><span class="done"></span><span class="num">12</span></div>
    <div class="todo-row"><span class="write"></span><span class="done"></span><span class="num">13</span></div>
    <div class="todo-row"><span class="write"></span><span class="done"></span><span class="num">14</span></div>
    <div class="todo-row"><span class="write"></span><span class="done"></span><span class="num">15</span></div>
    <div class="todo-row"><span class="write"></span><span class="done"></span><span class="num">16</span></div>
    <div class="todo-row"><span class="write"></span><span class="done"></span><span class="num">17</span></div>
    <div class="todo-row"><span class="write"></span><span class="done"></span><span class="num">18</span></div>
    <div class="todo-row"><span class="write"></span><span class="done"></span><span class="num">19</span></div>
    <div class="todo-row"><span class="write"></span><span class="done"></span><span class="num">20</span></div>
    <div class="todo-row"><span class="write"></span><span class="done"></span><span class="num">21</span></div>
    <div class="todo-row todo-row--pink"><span class="write"><span>Communication/comments:</span><span>Notes / Permission Forms / Newsletter received:</span></span><span class="num">22</span></div>
    <div class="todo-row todo-row--pink"><span class="write"></span><span class="num">23</span></div>
    <div class="todo-row todo-row--pink"><span class="write"></span><span class="num">24</span></div>
    <div class="todo-row todo-row--pink"><span class="write"><span>Teacher:</span><span style="margin-right:170px">Parent / Guardian:</span></span><span class="num">25</span></div>
  </div>
</div>
<div class="abs texture illus-hand" role="img" aria-label="Faint sketch of a hand holding a pen"></div>

<div class="abs this-week"><b>This week:</b> On August 27th, 1910, Ada Brightwell was born, Nobel Prize winner.</div>
<div class="abs folio" style="left:1128px;top:752px">97</div>

</body>
</html>
```